Business Stationery Design

I would like to get some stationery designed for my company. The stationery should include a letterhead, envelope, and business card. We are a technology consulting company specializing in Healthcare IT, and Education management systems. The colors of the stationery should match the logo. The logo is uploaded.

Target Market(s)

Hospitals, Clinics. Doctors offices. Private Schools.

Industry/Entity Type

Business

```html
<!DOCTYPE html>
<html lang="en">
<head>
<meta charset="utf-8">
<title>Larkfield Advisory Group – Stationery</title>
<link href="https://fonts.googleapis.com/css2?family=Open+Sans:wght@400;600;700&family=Arimo:wght@400;700&display=swap" rel="stylesheet">
<style>
  :root{
    --bg:#c4c4c4;
    --paper:#ffffff;
    --green:#6cbd45;
    --green-dark:#5aa536;
    --green-faint:#eef5e8;
    --yellow:#f4b31a;
    --ink:#222222;
    --body:#7a7a7a;
  }
  *{margin:0;padding:0;box-sizing:border-box}
  html,body{width:1200px;height:900px;overflow:hidden;background:var(--bg)}
  .canvas{position:relative;width:1200px;height:900px;font-family:"Open Sans",Arial,sans-serif;color:var(--ink)}
  .sheet{position:absolute;background:var(--paper);overflow:hidden}
  .sheet svg.decor{position:absolute;left:0;top:0}

  .brand{position:absolute;display:flex;flex-direction:column;align-items:flex-start}
  .brand-mark{width:34px;height:34px;border-radius:50%;background:var(--green);margin-bottom:6px}
  .brand-name{font-family:"Open Sans",sans-serif;font-weight:400;color:var(--green);line-height:1}
  .brand-sub{font-family:"Open Sans",sans-serif;font-weight:400;color:var(--green);line-height:1;margin-top:2px}
  .brand.light .brand-mark{background:#fff}
  .brand.light .brand-name,.brand.light .brand-sub{color:#fff}

  .contact{position:absolute;font-size:10px;line-height:13px;color:var(--ink)}
  .contact li{list-style:none;display:flex;align-items:center;gap:5px}
  .icon{width:10px;height:10px;border-radius:50%;background:var(--green);display:inline-flex;align-items:center;justify-content:center;flex:none}
  .icon svg{width:6px;height:6px}
  .divider{position:absolute;width:1px;background:var(--yellow)}
  .address{position:absolute;font-size:10px;line-height:13px}
  .web{position:absolute;font-size:9.5px;font-weight:600;color:var(--ink)}

  /* letterhead */
  .letterhead{left:103px;top:83px;width:487px;height:687px}
  .letter-body{position:absolute;left:26px;top:198px;width:436px;font-family:"Arimo",Arial,sans-serif;color:var(--body);font-size:10.6px;line-height:12.6px;text-align:justify}
  .letter-body .salutation{font-weight:700;color:#555;font-size:12.5px;margin-bottom:12px}
  .letter-body p{margin-bottom:12px}
  .signature{position:absolute;left:26px;top:440px;width:100px;height:40px;background:linear-gradient(90deg,#e6e6e6,#f4f4f4);border-radius:4px}
</style>
</head>
<body>
<div class="canvas">

  <!-- Letterhead -->
  <section class="sheet letterhead">
    <svg class="decor" width="487" height="687" viewBox="0 0 487 687">
      <circle cx="245" cy="590" r="150" fill="var(--green-faint)"/>
      <path d="M0 669 H335 L342 674 H0 Z" fill="var(--green)"/>
      <path d="M340 668 Q347 670 352 674 L345 687 H487 V668 Z" fill="var(--yellow)"/>
      <path d="M0 674 H352 L345 687 H0 Z" fill="#fff"/>
    </svg>
    <div class="brand" style="left:28px;top:46px">
      <span class="brand-mark"></span>
      <span class="brand-name" style="font-size:19px">Larkfield</span>
      <span class="brand-sub" style="font-size:7px;margin-left:24px">Advisory Group</span>
    </div>
    <span class="divider" style="left:333px;top:39px;height:66px"></span>
    <div class="address" style="left:345px;top:36px">418, Harbor Lane,<br>Oakdale, CA 95361</div>
    <ul class="contact" style="left:345px;top:66px">
      <li><span class="icon"></span>555 010 2234</li>
      <li><span class="icon"><svg viewBox="0 0 10 10"><path d="M2 1l2 2-1 1.5a6 6 0 0 0 2.5 2.5L7 6l2 2-1.5 1.5C4 9 1 6 .5 2.5z" fill="#fff"/></svg></span>555 010 2234</li>
      <li><span class="icon"></span>info@larkfieldgroup.com</li>
    </ul>
    <div class="letter-body">
      <p class="salutation">Dear Mr. Daniel,</p>
      <p>Lorem Ipsum is simply dummy text of the printing and typesetting industry. Lorem Ipsum has been the industry's standard dummy text ever since the 1500s, when an unknown printer took a galley of type and scrambled it to make a type specimen book. It has survived not only five centuries, but also the leap into electronic typesetting, remaining essentially unchanged.</p>
      <p>The standard chunk of Lorem Ipsum used since the 1500s is reproduced below for those interested. Sections 1.10.32 and 1.10.33 from "de Finibus Bonorum et Malorum" by Varenus are also reproduced in their exact original form, accompanied by English versions from the 1914 translation by H. Radley</p>
      <p>Lorem Ipsum is simply dummy text of the printing and typesetting industry. Lorem Ipsum has been the industry's standard dummy text ever since the 1500s, when an unknown printer took a galley of type and scrambled it to make a type specimen book. It has survived not only five centuries, but also the leap into electronic typesetting, remaining essentially unchanged. It was popularised in the</p>
    </div>
    <div class="signature" role="img" aria-label="Handwritten signature"></div>
    <span class="web" style="left:356px;top:672px">www.larkfieldgroup.com</span>
  </section>

  <!-- Compliment slip / DL sheet -->
  <section class="sheet" style="left:620px;top:103px;width:533px;height:230px">
    <svg class="decor" width="533" height="230" viewBox="0 0 533 230">
      <circle cx="415" cy="150" r="100" fill="var(--green-faint)"/>
      <path d="M0 215 H385 L392 219 H0 Z" fill="var(--green)"/>
      <path d="M390 213 Q397 214 402 219 L396 230 H533 V213 Z" fill="var(--yellow)"/>
      <path d="M0 219 H402 L396 230 H0 Z" fill="#fff"/>
    </svg>
    <div class="brand" style="left:30px;top:28px">
      <span class="brand-mark" style="width:32px;height:32px"></span>
      <span class="brand-name" style="font-size:17px">Larkfield</span>
      <span class="brand-sub" style="font-size:6.5px;margin-left:30px">Advisory Group</span>
    </div>
    <ul class="contact" style="left:26px;top:166px">
      <li><span class="icon"></span>555 010 2234</li>
      <li><span class="icon"></span>555 010 2234</li>
      <li><span class="icon"></span>info@larkfieldgroup.com</li>
    </ul>
    <span class="divider" style="left:153px;top:168px;height:36px"></span>
    <div class="address" style="left:170px;top:178px">418, Harbor Lane,<br>Oakdale, CA 95361</div>
    <span class="web" style="left:408px;top:216px">www.larkfieldgroup.com</span>
  </section>

  <!-- Envelope -->
  <section class="sheet" style="left:617px;top:353px;width:536px;height:234px">
    <svg class="decor" width="536" height="234" viewBox="0 0 536 234">
      <path d="M0 0 H536 V40 Q536 48 520 52 L290 93 Q268 97 246 93 L16 52 Q0 48 0 40 Z" fill="var(--green)"/>
    </svg>
    <div class="brand light" style="left:244px;top:24px">
      <span class="brand-mark" style="width:22px;height:22px;margin-bottom:3px;margin-left:10px"></span>
      <span class="brand-name" style="font-size:11px">Larkfield</span>
      <span class="brand-sub" style="font-size:4.5px;margin-left:19px">Advisory Group</span>
    </div>
  </section>

  <!-- Business card front -->
  <section class="sheet" style="left:622px;top:605px;width:259px;height:147px">
    <svg class="decor" width="259" height="147" viewBox="0 0 259 147">
      <line x1="12" y1="85" x2="248" y2="85" stroke="var(--yellow)" stroke-width="0.6"/>
      <path d="M0 134 H165 L170 137 H0 Z" fill="var(--green)"/>
      <path d="M168 133 Q172 134 175 137 L171 147 H259 V133 Z" fill="var(--yellow)"/>
      <path d="M0 137 H175 L171 147 H0 Z" fill="#fff"/>
    </svg>
    <div class="brand" style="left:16px;top:18px">
      <span class="brand-mark" style="width:26px;height:26px;margin-bottom:4px"></span>
      <span class="brand-name" style="font-size:13px">Larkfield</span>
      <span class="brand-sub" style="font-size:5px;margin-left:22px">Advisory Group</span>
    </div>
    <div style="position:absolute;right:12px;top:73px;text-align:right">
      <div style="font-size:8.5px;font-weight:700;color:var(--green-dark)">DANIEL REYES</div>
      <div style="font-size:6.5px;color:var(--yellow)">Owner</div>
    </div>
    <ul class="contact" style="left:12px;top:94px;font-size:7px;line-height:10px">
      <li><span class="icon" style="width:7px;height:7px"></span>555 010 2234</li>
      <li><span class="icon" style="width:7px;height:7px"></span>555 010 2234</li>
      <li><span class="icon" style="width:7px;height:7px"></span>info@larkfieldgroup.com</li>
    </ul>
    <div class="address" style="right:12px;top:106px;font-size:7px;line-height:10px;text-align:right">418, Harbor Lane,<br>Oakdale, CA 95361</div>
    <span class="web" style="left:170px;top:135px;font-size:6.5px">www.larkfieldgroup.com</span>
  </section>

  <!-- Business card back -->
  <section class="sheet" style="left:894px;top:605px;width:259px;height:147px;background:var(--green)">
    <div role="img" aria-label="Dotted world map" style="position:absolute;left:6px;top:8px;width:247px;height:112px;border-radius:40px;background:radial-gradient(ellipse at center,rgba(90,165,54,.55),rgba(108,189,69,0) 70%)"></div>
    <div class="brand light" style="left:100px;top:54px">
      <span class="brand-mark" style="width:26px;height:26px;margin-bottom:4px;margin-left:14px"></span>
      <span class="brand-name" style="font-size:14px">Larkfield</span>
      <span class="brand-sub" style="font-size:5.5px;margin-left:22px">Advisory Group</span>
    </div>
    <svg class="decor" width="259" height="147" viewBox="0 0 259 147">
      <line x1="62" y1="137" x2="86" y2="137" stroke="#fff" stroke-width=".5"/>
      <line x1="173" y1="137" x2="197" y2="137" stroke="#fff" stroke-width=".5"/>
    </svg>
    <span class="web" style="left:88px;top:132px;font-size:6.5px;font-weight:400;color:#fff">www.larkfieldgroup.com</span>
  </section>

</div>
</body>
</html>
```